Business Card Design Project

I am a psychotherapist, counselor and expressive arts therapist (means I use every art form imaginable in the service of healing). I'm just starting out in private practice in San Francisco, CA. I work with individual adults, children and families. I'd like the card to mirror the simplicity and color palate of my website. I also would love if there is a symbol, image of fire, flame or spark (that is warming, not frightening).

Check out my website: www.lorabecketmft.com

I want the cards to be printed in letter press so please keep that in mind!

Target Market(s)

Upper Middle Class Adults who are progressively minded, artistic or artists, open to psychotherapy, interested in health & healing.

Industry/Entity Type

Business

Requirements
Must have
• Text to be included:

Lora Becket
Counseling, Psychotherapy & Expressive Arts

2914 Alderwood Avenue, Suite D
San Francisco, CA 94127
p. 415.206.3791
lorajanebecket@meadowpost.net

www.lorabecketmft.com

MFT License Number 48671

It's OK to abbreviate Number to # or Street to St., etc.

Must be compatible with letter press printing.
Nice to have
• I don't have a logo. I don't expect designers to necessarily create one for me, but if someone comes up with a simple image (see above about flame), that would be great. I don't have much of a budget now, but expect that to change in the next year or so and then could buy a logo for my website, future letterhead, etc.

```html
<!DOCTYPE html>
<html lang="en">
<head>
<meta charset="utf-8">
<title>Lora Becket – Business Card</title>
<link rel="stylesheet" href="https://fonts.googleapis.com/css2?family=Mulish:ital,wght@0,400;0,700;1,400&display=swap">
<style>
  :root {
    --page-bg: #3a3a3a;
    --card-bg: #000000;
    --gold: #f2a900;
    --text-light: #e8e8e8;
    --flame-orange: #f08a24;
    --flame-red: #a3101e;
    --flame-deep: #3a0208;
    --pill-bg: #f5b21a;
    --pill-text: #3a2600;
  }
  * { margin: 0; padding: 0; box-sizing: border-box; }
  html, body {
    width: 1200px;
    height: 900px;
    overflow: hidden;
    background: var(--page-bg);
    font-family: "Mulish", "Century Gothic", sans-serif;
  }
  .business-card {
    position: absolute;
    left: 100px;
    top: 172px;
    width: 1000px;
    height: 556px;
    border-radius: 36px;
    background: var(--card-bg);
    overflow: hidden;
  }
  .identity {
    position: absolute;
    left: 76px;
    top: 66px;
  }
  .identity__name {
    color: var(--gold);
    font-weight: 700;
    font-size: 42px;
    line-height: 1.1;
  }
  .identity__practice {
    margin-top: 8px;
    color: var(--text-light);
    font-style: italic;
    font-size: 27px;
    line-height: 1.25;
  }
  .contact-list {
    position: absolute;
    left: 76px;
    top: 336px;
    list-style: none;
    color: var(--text-light);
    font-size: 27px;
    line-height: 32px;
  }
  .contact-list__item {
    display: flex;
    align-items: flex-start;
  }
  .contact-list__icon {
    flex: 0 0 22px;
    width: 22px;
    height: 22px;
    margin-top: 5px;
    margin-right: 11px;
  }
  .flame-mark {
    position: absolute;
    left: 548px;
    top: 42px;
    width: 416px;
    height: 514px;
    background:
      radial-gradient(ellipse 45% 30% at 62% 18%, var(--flame-orange), transparent 75%),
      radial-gradient(ellipse 60% 70% at 55% 70%, var(--flame-red), transparent 80%),
      linear-gradient(to bottom, transparent 30%, var(--flame-deep) 100%);
    border-radius: 50% 50% 10% 10% / 60% 60% 10% 10%;
  }
  .license-badge {
    position: absolute;
    left: 646px;
    top: 472px;
    width: 220px;
    height: 32px;
    border-radius: 16px;
    background: var(--pill-bg);
    color: var(--pill-text);
    font-size: 19px;
    line-height: 32px;
    text-align: center;
  }
</style>
</head>
<body>
  <div class="business-card">
    <div class="identity">
      <h1 class="identity__name">Lora Becket</h1>
      <p class="identity__practice">Counseling, Psychotherapy<br>&amp; Expressive Arts</p>
    </div>

    <ul class="contact-list">
      <li class="contact-list__item">
        <svg class="contact-list__icon" viewBox="0 0 22 22" aria-hidden="true">
          <path d="M11 1a7 7 0 0 0-7 7c0 5 7 13 7 13s7-8 7-13a7 7 0 0 0-7-7z" fill="var(--gold)"/>
          <circle cx="11" cy="8" r="2.6" fill="var(--card-bg)"/>
        </svg>
        <span>2914 Alderwood Avenue, Suite D<br>San Francisco, CA 94127</span>
      </li>
      <li class="contact-list__item">
        <svg class="contact-list__icon" viewBox="0 0 22 22" aria-hidden="true">
          <circle cx="11" cy="11" r="10" fill="var(--gold)"/>
          <path d="M8 6l2 2-1.2 1.5c.8 1.6 2 2.8 3.7 3.7L14 12l2 2-1.5 2c-3.5-.3-7.2-4-7.5-7.5z" fill="var(--card-bg)"/>
        </svg>
        <span>415 206 3791</span>
      </li>
      <li class="contact-list__item">
        <svg class="contact-list__icon" viewBox="0 0 22 22" aria-hidden="true">
          <rect x="2" y="6" width="18" height="11" fill="var(--gold)"/>
          <path d="M2 6l9 6 9-6" fill="none" stroke="var(--card-bg)" stroke-width="1.5"/>
        </svg>
        <span>lorajanebecket@meadowpost.net</span>
      </li>
      <li class="contact-list__item">
        <svg class="contact-list__icon" viewBox="0 0 22 22" aria-hidden="true">
          <circle cx="11" cy="11" r="9" fill="var(--gold)"/>
          <g fill="none" stroke="var(--card-bg)" stroke-width="1.3">
            <ellipse cx="11" cy="11" rx="4" ry="9"/>
            <path d="M2 11h18M3.5 6.5h15M3.5 15.5h15"/>
          </g>
        </svg>
        <span>www.lorabecketmft.com</span>
      </li>
    </ul>

    <div class="flame-mark" role="img" aria-label="Warm flame illustration in orange and deep red"></div>

    <div class="license-badge">MFT License # 48671</div>
  </div>
</body>
</html>
```